Korvane Sky Works, LLC - Business Card

I currently have a drone business that specializes in aerial photography, thermal image inspections, deer recovery, search and rescue, custom agricultural applications. i will attach my current business card as well as some logos to incorporate for a new up to date business card
Updates

Designs look the same

Sick

Target Market(s)

farmers, hunters

Contact Information for Business Card

name address phone number (as existing card i attached)

Requirements
Must have
• im good with existing business card, but would like an agricultural twist

```html
<!DOCTYPE html>
<html lang="en">
<head>
<meta charset="utf-8">
<title>Korvane Sky Works, LLC – Business Card</title>
<link rel="stylesheet" href="https://fonts.googleapis.com/css2?family=Montserrat:wght@400;500;700;800&display=swap">
<style>
  :root {
    --stage: #2b2b2d;
    --card: #060708;
    --green: #44a340;
    --green-deep: #2f7f2c;
    --ink: #f4f4f4;
  }
  * { margin: 0; padding: 0; box-sizing: border-box; }
  html, body { width: 1200px; height: 988px; overflow: hidden; }
  body {
    background: var(--stage);
    font-family: "Montserrat", sans-serif;
    color: var(--ink);
    display: flex;
    flex-direction: column;
    align-items: center;
    justify-content: center;
    gap: 36px;
  }
  .card {
    position: relative;
    width: 770px;
    height: 440px;
    background: var(--card);
    border: 8px solid var(--green);
    border-radius: 40px;
    overflow: hidden;
  }
  .brand {
    display: flex;
    align-items: center;
    gap: 14px;
    font-weight: 800;
    color: var(--green);
    letter-spacing: 1px;
    text-transform: uppercase;
  }
  .brand__dot {
    width: 26px; height: 26px;
    border-radius: 50%;
    background: var(--green);
    flex: none;
  }
  /* Front */
  .card--front .brand {
    position: absolute;
    left: 50%; top: 120px;
    transform: translateX(-50%);
    font-size: 52px;
  }
  .services {
    position: absolute;
    left: 0; right: 0; top: 270px;
    list-style: none;
    display: flex;
    flex-wrap: wrap;
    justify-content: center;
    gap: 12px 26px;
    padding: 0 90px;
    font-size: 22px;
    font-weight: 500;
  }
  .services li { display: flex; align-items: center; gap: 10px; }
  .services li::before {
    content: ""; width: 9px; height: 9px; border-radius: 50%;
    background: var(--green);
  }
  /* Back */
  .card--back .brand {
    position: absolute;
    left: 70px; top: 190px;
    font-size: 40px;
  }
  .divider {
    position: absolute;
    left: 400px; top: 80px;
    width: 2px; height: 280px;
    background: var(--green);
  }
  .contact {
    position: absolute;
    left: 440px; top: 70px;
  }
  .contact__name {
    font-size: 32px; font-weight: 800;
    color: var(--green); text-transform: uppercase; letter-spacing: .5px;
  }
  .contact__role { font-size: 17px; font-weight: 500; margin-top: 2px; letter-spacing: 1px; }
  .contact__address { font-size: 18px; margin-top: 30px; line-height: 1.35; font-style: normal; }
  .contact__list { list-style: none; margin-top: 10px; font-size: 18px; }
  .contact__list li { display: flex; align-items: center; gap: 12px; line-height: 1.8; }
  .contact__list svg { width: 16px; height: 16px; fill: var(--green); flex: none; }
</style>
</head>
<body>

<section class="card card--front" aria-label="Card front">
  <div class="brand"><span class="brand__dot"></span>Korvane</div>
  <ul class="services">
    <li>Thermal Image Inspections</li>
    <li>Deer Recovery</li>
    <li>Search &amp; Rescue</li>
    <li>Real Estate Photography</li>
  </ul>
</section>

<section class="card card--back" aria-label="Card back">
  <div class="brand"><span class="brand__dot"></span>Korvane</div>
  <div class="divider"></div>
  <div class="contact">
    <p class="contact__name">Dalen Morrow</p>
    <p class="contact__role">OWNER</p>
    <address class="contact__address">214 W. Orchard St.<br>Fenwick, OH 45900</address>
    <ul class="contact__list">
      <li><svg viewBox="0 0 16 16" aria-hidden="true"><path d="M3.5 1l2.5 3-1.5 1.5c.8 2 2.5 3.7 4.5 4.5L10.5 8.5l3 2.5-1.5 3C7 14 2 9 2 3.5z"/></svg>419-555-0142</li>
      <li><svg viewBox="0 0 16 16" aria-hidden="true"><path d="M1 3h14v10H1z M1.5 3.5L8 9l6.5-5.5" stroke="#060708" stroke-width="1.2"/></svg>korvaneskyworks@mail.com</li>
      <li><svg viewBox="0 0 16 16" aria-hidden="true"><circle cx="8" cy="8" r="7"/><path d="M1 8h14M8 1c-3 3.5-3 10.5 0 14M8 1c3 3.5 3 10.5 0 14" stroke="#060708" stroke-width="1" fill="none"/></svg>www.korvaneskyworks.com</li>
    </ul>
  </div>
</section>

</body>
</html>
```